Outpost Lattice Advisors – Franchise Growth & Development Presentation

Outpost Lattice Advisors is an outsourced franchise sales organization (FSO) that helps franchisors grow their franchise systems without the expense and risk of hiring an internal franchise development team.

We are seeking a professional PowerPoint presentation that will be used to present our services to franchisors, franchise executives, founders, and growth-stage franchise brands.

The presentation should communicate the value of partnering with Outpost Lattice Advisors, including:

• Fractional franchise sales team versus hiring internal staff
• 30+ years of franchise industry experience
• 550+ franchise sales successes
• Immediate access to established franchise broker relationships
• Proven franchise development processes
• Franchise growth strategy and enterprise value creation
• Potential private equity and exit opportunities through franchise expansion

The presentation should feel like a modern consulting, investment, or growth strategy presentation rather than a typical sales brochure. We want strong visual storytelling, custom infographics, professional diagrams, and clean business-oriented design.

The audience includes business owners, franchise founders, franchise executives, and investors who are evaluating growth strategies for their franchise systems.

Target Market(s)

Primary Audience: Emerging franchisors Growth-stage franchise brands Franchise founders Franchise CEOs Franchise presidents Franchise development executives Secondary Audience: Private equity firms Franchise investors Strategic buyers Franchise consultants

Industry/Entity Type

Franchise Development, Private Equity / Business Expansion

Font styles to use
Other font styles liked:
• Use Montserrat for titles and Open Sans for body text.

Requirements
Must have
• Modern professional business design Consistent branding throughout Custom infographics Comparison graphics Broker network ecosystem graphic Enterprise value graphic Easy-to-read charts and visuals Editable PowerPoint format Professional iconography. www.outpostlatticeadvisors.example as reference for colors
Nice to have
• Franchise-related imagery Subtle growth-themed visuals Timeline graphics Data visualization Private equity / valuation style graphics
Should not have
• Cartoon graphics Clip art Overly busy slides Stock-template appearance Bright neon colors Handwritten fonts Excessive text on slides Juvenile or playful design elements

```html
<!DOCTYPE html>
<html lang="en">
<head>
<meta charset="utf-8">
<title>Outpost Lattice Advisors – Presentation Overview</title>
<link href="https://fonts.googleapis.com/css2?family=Montserrat:wght@500;600;700;800&family=Open+Sans:ital,wght@0,400;0,600;0,700;1,400&display=swap" rel="stylesheet">
<style>
:root{
  --navy:#13294b;
  --navy-2:#1b3660;
  --navy-3:#23406f;
  --blue:#2f5f9e;
  --orange:#f39200;
  --orange-soft:#f6b24a;
  --paper:#f3f5f8;
  --card:#ffffff;
  --line:#e2e6ec;
  --ink:#1d2a3d;
  --muted:#6b7686;
  --canvas:#ffffff;
}
*{margin:0;padding:0;box-sizing:border-box}
html,body{width:1200px;height:848px;overflow:hidden;background:var(--canvas)}
.stage{position:absolute;left:0;top:0;width:2292px;height:1620px;transform:scale(.52356);transform-origin:0 0;font-family:"Open Sans",sans-serif;color:var(--ink)}
.slide{position:absolute;width:461px;height:260px;overflow:hidden;background:var(--paper)}
.slide.dark{background:var(--navy);color:#fff}
.abs{position:absolute}
.eyebrow{position:absolute;left:21px;top:21px;font:700 5px "Montserrat",sans-serif;color:var(--orange);letter-spacing:.2px;text-transform:uppercase}
.title{position:absolute;left:21px;top:30px;font:700 14px/1.15 "Montserrat",sans-serif;color:var(--navy)}
.dark .title{color:#fff}
.brand{position:absolute;right:11px;top:8px;font:700 5.5px "Montserrat",sans-serif;color:#8a93a0;letter-spacing:.3px;text-align:right;border-bottom:.5px solid #c5cad2;padding-bottom:1px}
.dark .brand{color:#7f8ea8;border-color:#4b5f82}
.brand-foot{position:absolute;left:21px;bottom:10px;font:700 6px "Montserrat",sans-serif;color:#fff;letter-spacing:.3px}
.foot{position:absolute;bottom:7px;font-size:3px;color:#9aa3b0}
.foot.l{left:21px}.foot.r{right:21px}
.dark .foot{color:#6f80a0}
.lead{position:absolute;font-size:4.2px;line-height:1.5;color:var(--muted)}
.dark .lead{color:#b9c4d8}
.card{position:absolute;background:var(--card);border:.5px solid var(--line);border-radius:3px;box-shadow:0 1px 3px rgba(19,41,75,.08)}
.dcard{position:absolute;background:var(--navy-2);border:.5px solid #2d4a78;border-radius:3px}
.ico{display:flex;align-items:center;justify-content:center;border-radius:50%;background:var(--orange)}
.ico svg{width:55%;height:55%;fill:none;stroke:#fff;stroke-width:2.2;stroke-linecap:round;stroke-linejoin:round}
.ct{font:700 5.8px/1.15 "Montserrat",sans-serif;color:var(--navy)}
.dark .ct{color:#fff}
.cx{font-size:3.3px;line-height:1.45;color:var(--muted)}
.dark .cx{color:#aab6cc}
.center{text-align:center}
.stat{font:700 12px "Montserrat",sans-serif;color:var(--orange)}
</style>
</head>
<body>
<svg width="0" height="0" style="position:absolute">
  <defs>
    <symbol id="i-people" viewBox="0 0 24 24"><circle cx="9" cy="8" r="3"/><path d="M3 19c0-3 3-5 6-5s6 2 6 5"/><circle cx="17" cy="9" r="2.5"/><path d="M16 14c3 0 5 2 5 4"/></symbol>
    <symbol id="i-chart" viewBox="0 0 24 24"><path d="M4 20V4M4 20h16M7 15l4-4 3 3 5-6"/></symbol>
    <symbol id="i-target" viewBox="0 0 24 24"><circle cx="12" cy="12" r="8"/><circle cx="12" cy="12" r="4"/><circle cx="12" cy="12" r="1"/></symbol>
    <symbol id="i-loop" viewBox="0 0 24 24"><path d="M12 12c-2-3-4-4-6-4a4 4 0 0 0 0 8c2 0 4-1 6-4s4-4 6-4a4 4 0 0 1 0 8c-2 0-4-1-6-4z"/></symbol>
    <symbol id="i-cal" viewBox="0 0 24 24"><rect x="4" y="5" width="16" height="15" rx="2"/><path d="M4 10h16M8 3v4M16 3v4"/></symbol>
    <symbol id="i-medal" viewBox="0 0 24 24"><circle cx="12" cy="9" r="5"/><path d="M9 13l-2 8 5-3 5 3-2-8"/></symbol>
    <symbol id="i-net" viewBox="0 0 24 24"><circle cx="6" cy="6" r="2.5"/><circle cx="18" cy="6" r="2.5"/><circle cx="12" cy="18" r="2.5"/><path d="M8 7l8 0M7 8l4 8M17 8l-4 8"/></symbol>
    <symbol id="i-layers" viewBox="0 0 24 24"><path d="M12 3l9 5-9 5-9-5z"/><path d="M3 13l9 5 9-5"/></symbol>
    <symbol id="i-cash" viewBox="0 0 24 24"><rect x="3" y="7" width="18" height="11" rx="2"/><circle cx="12" cy="12.5" r="2.5"/></symbol>
    <symbol id="i-hour" viewBox="0 0 24 24"><path d="M6 3h12M6 21h12M7 3c0 5 10 7 10 9s-10 4-10 9M17 3c0 5-10 7-10 9s10 4 10 9"/></symbol>
    <symbol id="i-warn" viewBox="0 0 24 24"><path d="M12 4l9 16H3z"/><path d="M12 10v4M12 17v.5"/></symbol>
    <symbol id="i-bolt" viewBox="0 0 24 24"><path d="M13 3L5 14h6l-1 7 8-11h-6z"/></symbol>
    <symbol id="i-shield" viewBox="0 0 24 24"><path d="M12 3l8 3v6c0 5-4 8-8 9-4-1-8-4-8-9V6z"/></symbol>
    <symbol id="i-share" viewBox="0 0 24 24"><circle cx="6" cy="12" r="2.5"/><circle cx="18" cy="6" r="2.5"/><circle cx="18" cy="18" r="2.5"/><path d="M8 11l8-4M8 13l8 4"/></symbol>
    <symbol id="i-user" viewBox="0 0 24 24"><circle cx="12" cy="8" r="4"/><path d="M4 21c0-4 4-6 8-6s8 2 8 6"/></symbol>
    <symbol id="i-door" viewBox="0 0 24 24"><path d="M6 21V4h12v17M4 21h16M14 12v1"/></symbol>
    <symbol id="i-search" viewBox="0 0 24 24"><circle cx="10" cy="10" r="6"/><path d="M15 15l5 5"/></symbol>
    <symbol id="i-mega" viewBox="0 0 24 24"><path d="M4 10v4h3l8 5V5L7 10z"/><path d="M18 9c1 1 1 5 0 6"/></symbol>
    <symbol id="i-trophy" viewBox="0 0 24 24"><path d="M7 4h10v5a5 5 0 0 1-10 0z"/><path d="M12 14v4M8 20h8M7 6H4c0 3 1 4 3 4M17 6h3c0 3-1 4-3 4"/></symbol>
    <symbol id="i-check" viewBox="0 0 24 24"><path d="M6 12l4 4 8-8"/></symbol>
    <symbol id="i-gem" viewBox="0 0 24 24"><path d="M6 4h12l3 5-9 11L3 9z"/><path d="M3 9h18"/></symbol>
    <symbol id="i-gear" viewBox="0 0 24 24"><circle cx="12" cy="12" r="3"/><path d="M12 3v3M12 18v3M3 12h3M18 12h3M5.6 5.6l2 2M16.4 16.4l2 2M5.6 18.4l2-2M16.4 7.6l2-2"/></symbol>
    <symbol id="i-globe" viewBox="0 0 24 24"><circle cx="12" cy="12" r="8"/><path d="M4 12h16M12 4c3 3 3 13 0 16M12 4c-3 3-3 13 0 16"/></symbol>
    <symbol id="i-mail" viewBox="0 0 24 24"><rect x="3" y="6" width="18" height="12" rx="2"/><path d="M3 7l9 6 9-6"/></symbol>
    <symbol id="i-pin" viewBox="0 0 24 24"><path d="M12 21s-7-7-7-12a7 7 0 0 1 14 0c0 5-7 12-7 12z"/><circle cx="12" cy="9" r="2.5"/></symbol>
    <symbol id="i-doc" viewBox="0 0 24 24"><rect x="6" y="3" width="12" height="18" rx="2"/><path d="M9 8h6M9 12h6M9 16h4"/></symbol>
    <symbol id="i-rocket" viewBox="0 0 24 24"><path d="M14 4c4 0 6 2 6 6l-7 7-6-6z"/><path d="M7 11l-3 1 2 2M13 17l-1 3-2-2"/></symbol>
  </defs>
</svg>

<main class="stage">

<!-- 1 Cover -->
<section class="slide dark" style="left:148px;top:109px">
  <div class="eyebrow" style="top:52px">Franchise Sales · Development · Growth Strategy</div>
  <h1 class="abs" style="left:21px;top:66px;font:700 26px/1.2 'Montserrat',sans-serif;color:#fff">Outpost Lattice<br>Advisors</h1>
  <p class="lead" style="left:21px;top:144px;width:240px;color:#d3dbe8">Your outsourced franchise sales team — built to scale brands, create enterprise value, and unlock exit opportunities.</p>
  <div class="dcard" style="left:21px;top:191px;width:104px;height:37px;padding:6px 5px"><div class="stat" style="font-size:10px">30+</div><div class="cx">Years of experience</div></div>
  <div class="dcard" style="left:134px;top:191px;width:104px;height:37px;padding:6px 5px"><div class="stat" style="font-size:10px">550+</div><div class="cx">Franchise sales</div></div>
  <div class="dcard" style="left:247px;top:191px;width:104px;height:37px;padding:6px 5px"><div class="stat" style="font-size:10px">National</div><div class="cx">Broker network</div></div>
  <div class="foot r" style="bottom:11px">outpostlatticeadvisors.example</div>
</section>

<!-- 2 Challenge -->
<section class="slide" style="left:682px;top:109px">
  <div role="img" aria-label="Soft-focus office photograph of a franchise team at work" class="abs" style="left:0;top:0;width:461px;height:260px;background:linear-gradient(100deg,#eef1f5 0%,#e6eaef 45%,#d8dee6 75%,#cdd4dc 100%)"></div>
  <div class="brand">OUTPOST LATTICE ADVISORS</div>
  <div class="eyebrow">The Challenge</div>
  <h2 class="title" style="top:32px">Franchise growth stalls without<br>a dedicated sales engine</h2>
  <p class="lead" style="left:21px;top:80px;width:210px">Most emerging and growth-stage brands face the same bottleneck: demand for the franchise exists, but there is no consistent, professional engine converting interest into qualified, awarded franchisees.</p>
  <p class="lead" style="left:21px;top:128px;width:210px">Building that capability internally is slow, expensive, and concentrated in a single hire — a high-risk way to fund your most important growth lever.</p>
  <div class="card" style="left:254px;top:54px;width:186px;height:53px;padding:8px 8px 0 38px"><div class="ico abs" style="left:10px;top:9px;width:20px;height:20px"><svg><use href="#i-cash"/></svg></div><div class="ct">High fixed cost</div><div class="cx" style="margin-top:2px">A full-time development hire carries a six-figure salary, benefits, tools, and ramp before a single deal closes.</div></div>
  <div class="card" style="left:254px;top:115px;width:186px;height:52px;padding:8px 8px 0 38px"><div class="ico abs" style="left:10px;top:9px;width:20px;height:20px"><svg><use href="#i-hour"/></svg></div><div class="ct">Slow to productive</div><div class="cx" style="margin-top:2px">Recruiting, onboarding, and earning broker trust can take 12–18 months to reach a producing pipeline.</div></div>
  <div class="card" style="left:254px;top:174px;width:186px;height:54px;padding:8px 8px 0 38px"><div class="ico abs" style="left:10px;top:9px;width:20px;height:20px"><svg><use href="#i-warn"/></svg></div><div class="ct">Concentrated risk</div><div class="cx" style="margin-top:2px">One hire is one point of failure. Turnover resets your pipeline and stalls momentum overnight.</div></div>
  <div class="foot l">Outpost Lattice Advisors</div><div class="foot r">outpostlatticeadvisors.example &nbsp; <span style="color:var(--orange)">02</span></div>
</section>

<!-- 3 Who we are -->
<section class="slide" style="left:1216px;top:109px">
  <div class="brand">OUTPOST LATTICE ADVISORS</div>
  <div class="eyebrow">Who We Are</div>
  <h2 class="title" style="top:32px">An extension of your franchise<br>development team</h2>
  <p class="lead" style="left:21px;top:69px;width:400px">Outpost Lattice Advisors brings structure, speed, and consistency to your growth engine — operating as a dedicated, fully accountable franchise sales function without the cost and risk of building one internally.</p>
  <div class="card center" style="left:21px;top:104px;width:96px;height:101px;padding:13px 6px 0"><div class="ico" style="width:18px;height:18px;margin:0 auto 6px"><svg><use href="#i-people"/></svg></div><div class="ct">Broker-driven expertise</div><div class="cx" style="margin-top:3px">Decades of franchise broker and referral relationships driving qualified candidate flow.</div></div>
  <div class="card center" style="left:128px;top:104px;width:96px;height:101px;padding:13px 6px 0"><div class="ico" style="width:18px;height:18px;margin:0 auto 6px"><svg><use href="#i-chart"/></svg></div><div class="ct">Performance-focused</div><div class="cx" style="margin-top:3px">Clear reporting, honest feedback, and accountability tied directly to results.</div></div>
  <div class="card center" style="left:235px;top:104px;width:96px;height:101px;padding:13px 6px 0"><div class="ico" style="width:18px;height:18px;margin:0 auto 6px"><svg><use href="#i-target"/></svg></div><div class="ct">Custom sales strategies</div><div class="cx" style="margin-top:3px">Tailored outreach and qualification aligned to your ideal franchisee profile.</div></div>
  <div class="card center" style="left:342px;top:104px;width:96px;height:101px;padding:13px 6px 0"><div class="ico" style="width:18px;height:18px;margin:0 auto 6px"><svg><use href="#i-loop"/></svg></div><div class="ct">Long-term partnership</div><div class="cx" style="margin-top:3px">We build a sustainable franchise sales system that scales with your brand.</div></div>
  <div class="foot l">Outpost Lattice Advisors</div><div class="foot r">outpostlatticeadvisors.example &nbsp; <span style="color:var(--orange)">03</span></div>
</section>

<!-- 4 Track record -->
<section class="slide dark" style="left:1749px;top:109px">
  <div class="eyebrow">Proven Track Record</div>
  <h2 class="title" style="top:32px">Three decades of franchise sales execution</h2>
  <p class="lead" style="left:21px;top:68px;width:330px">Our team has operated across the franchise development lifecycle — from broker activation to discovery day to award — building a record few internal hires can match.</p>
  <div class="dcard" style="left:21px;top:106px;width:97px;height:104px;padding:12px 9px"><div class="ico" style="width:16px;height:16px;margin-bottom:8px"><svg><use href="#i-cal"/></svg></div><div class="stat">30+</div><div class="cx" style="margin-top:4px">Years of franchise industry experience</div></div>
  <div class="dcard" style="left:128px;top:106px;width:97px;height:104px;padding:12px 9px"><div class="ico" style="width:16px;height:16px;margin-bottom:8px"><svg><use href="#i-medal"/></svg></div><div class="stat">550+</div><div class="cx" style="margin-top:4px">Franchise sales successes delivered</div></div>
  <div class="dcard" style="left:235px;top:106px;width:97px;height:104px;padding:12px 9px"><div class="ico" style="width:16px;height:16px;margin-bottom:8px"><svg><use href="#i-net"/></svg></div><div class="stat">National</div><div class="cx" style="margin-top:4px">Established franchise broker network</div></div>
  <div class="dcard" style="left:342px;top:106px;width:97px;height:104px;padding:12px 9px"><div class="ico" style="width:16px;height:16px;margin-bottom:8px"><svg><use href="#i-layers"/></svg></div><div class="stat" style="font-size:10px;line-height:14px">Multi-sector</div><div class="cx" style="margin-top:4px">Brands across diverse franchise categories</div></div>
  <div class="brand-foot">OUTPOST LATTICE ADVISORS</div>
  <div class="foot r">outpostlatticeadvisors.example &nbsp; <span style="color:var(--orange)">04</span></div>
</section>

<!-- 5 Comparison -->
<section class="slide" style="left:148px;top:490px">
  <div class="brand">OUTPOST LATTICE ADVISORS</div>
  <div class="eyebrow">The Fractional Advantage</div>
  <h2 class="title" style="top:32px">A fractional sales team vs. an internal hire</h2>
  <div class="abs" style="left:21px;top:98px;width:409px;height:150px;font-size:3.6px">
    <div class="abs" style="left:0;top:0;width:409px;height:17px;background:#e8ecf1"></div>
    <div class="abs" style="left:0;top:43px;width:409px;height:17px;background:#e8ecf1"></div>
    <div class="abs" style="left:0;top:86px;width:409px;height:17px;background:#e8ecf1"></div>
    <div class="abs" style="left:0;top:129px;width:409px;height:17px;background:#e8ecf1"></div>
  </div>
  <div class="abs" style="left:135px;top:76px;width:146px;height:172px;background:var(--navy);border-radius:2px"></div>
  <div class="abs center" style="left:135px;top:82px;width:146px;font:600 5px 'Montserrat',sans-serif;color:var(--orange)">FRACTIONAL TEAM<div style="font:400 2.8px 'Open Sans',sans-serif;color:#9fb0cc;margin-top:2px">Outpost Lattice Advisors</div></div>
  <div class="abs center" style="left:290px;top:82px;width:140px;font:600 4.5px 'Montserrat',sans-serif;color:#7c8796">INTERNAL HIRE<div style="font:400 2.8px 'Open Sans',sans-serif;margin-top:2px">In-house development staff</div></div>
  <div class="abs" style="left:21px;top:103px;font:700 3.6px/21.5px 'Montserrat',sans-serif;color:var(--navy)">Cost structure<br>Time to productive<br>Industry experience<br>Broker network<br>Team bandwidth<br>Execution risk<br>Scalability</div>
  <div class="abs" style="left:143px;top:103px;font-size:3.2px;line-height:21.5px;color:#fff">
    <div><span style="display:inline-block;width:4.5px;height:4.5px;border-radius:50%;background:var(--orange);vertical-align:middle;margin-right:4px"></span>Variable — aligned to performance</div>
    <div><span style="display:inline-block;width:4.5px;height:4.5px;border-radius:50%;background:var(--orange);vertical-align:middle;margin-right:4px"></span>Producing in weeks</div>
    <div><span style="display:inline-block;width:4.5px;height:4.5px;border-radius:50%;background:var(--orange);vertical-align:middle;margin-right:4px"></span>30+ years, on day one</div>
    <div><span style="display:inline-block;width:4.5px;height:4.5px;border-radius:50%;background:var(--orange);vertical-align:middle;margin-right:4px"></span>Established national relationships</div>
    <div><span style="display:inline-block;width:4.5px;height:4.5px;border-radius:50%;background:var(--orange);vertical-align:middle;margin-right:4px"></span>A full development team</div>
    <div><span style="display:inline-block;width:4.5px;height:4.5px;border-radius:50%;background:var(--orange);vertical-align:middle;margin-right:4px"></span>Diversified &amp; accountable</div>
    <div><span style="display:inline-block;width:4.5px;height:4.5px;border-radius:50%;background:var(--orange);vertical-align:middle;margin-right:4px"></span>Scales with your growth</div>
  </div>
  <div class="abs" style="left:292px;top:103px;font-size:3.2px;line-height:21.5px;color:#7c8796">
    <div><span style="display:inline-block;width:4.5px;height:4.5px;border-radius:50%;background:#c3c9d2;vertical-align:middle;margin-right:4px"></span>High fixed salary, benefits &amp; overhead</div>
    <div><span style="display:inline-block;width:4.5px;height:4.5px;border-radius:50%;background:#c3c9d2;vertical-align:middle;margin-right:4px"></span>12–18 months of ramp</div>
    <div><span style="display:inline-block;width:4.5px;height:4.5px;border-radius:50%;background:#c3c9d2;vertical-align:middle;margin-right:4px"></span>Limited to one individual</div>
    <div><span style="display:inline-block;width:4.5px;height:4.5px;border-radius:50%;background:#c3c9d2;vertical-align:middle;margin-right:4px"></span>Built slowly from scratch</div>
    <div><span style="display:inline-block;width:4.5px;height:4.5px;border-radius:50%;background:#c3c9d2;vertical-align:middle;margin-right:4px"></span>A single point of capacity</div>
    <div><span style="display:inline-block;width:4.5px;height:4.5px;border-radius:50%;background:#c3c9d2;vertical-align:middle;margin-right:4px"></span>One point of failure / turnover</div>
    <div><span style="display:inline-block;width:4.5px;height:4.5px;border-radius:50%;background:#c3c9d2;vertical-align:middle;margin-right:4px"></span>Re-hire to add capacity</div>
  </div>
  <div class="foot l">Outpost Lattice Advisors</div><div class="foot r">outpostlatticeadvisors.example &nbsp; <span style="color:var(--orange)">05</span></div>
</section>

<!-- 6 Economics -->
<section class="slide" style="left:682px;top:490px">
  <div class="brand">OUTPOST LATTICE ADVISORS</div>
  <div class="eyebrow">The Economics</div>
  <h2 class="title" style="top:32px">Lower cost. Faster to revenue.</h2>
  <div class="card" style="left:21px;top:74px;width:256px;height:159px">
    <div class="abs ct" style="left:10px;top:9px;font-size:4.6px">Illustrative franchise awards ramp — first 24 months</div>
    <svg class="abs" style="left:0;top:18px" width="256" height="140" viewBox="0 0 256 140">
      <g stroke="#e6e9ee" stroke-width=".4">
        <line x1="34" y1="12" x2="245" y2="12"/><line x1="34" y1="24" x2="245" y2="24"/><line x1="34" y1="36" x2="245" y2="36"/><line x1="34" y1="48" x2="245" y2="48"/><line x1="34" y1="60" x2="245" y2="60"/><line x1="34" y1="72" x2="245" y2="72"/><line x1="34" y1="84" x2="245" y2="84"/>
      </g>
      <line x1="34" y1="96" x2="245" y2="96" stroke="#9aa3b0" stroke-width=".5"/>
      <g font-size="3" fill="#7c8796" text-anchor="end">
        <text x="30" y="13">140</text><text x="30" y="25">120</text><text x="30" y="37">100</text><text x="30" y="49">80</text><text x="30" y="61">60</text><text x="30" y="73">40</text><text x="30" y="85">20</text><text x="30" y="97">0</text>
      </g>
      <g font-size="3" fill="#7c8796" text-anchor="middle">
        <text x="44" y="102">1</text><text x="74" y="102">2</text><text x="104" y="102">3</text><text x="134" y="102">4</text><text x="164" y="102">5</text><text x="194" y="102">6</text><text x="226" y="102">7</text><text x="135" y="109">Months</text>
      </g>
      <text x="14" y="60" font-size="2.8" fill="#7c8796" transform="rotate(-90 14 60)" text-anchor="middle">Cumulative awards</text>
      <polyline fill="none" stroke="#d98a1a" stroke-width="1" points="44,95 74,89 104,82 134,72 164,58 194,39 226,18"/>
      <g fill="#d98a1a"><circle cx="44" cy="95" r="1.2"/><circle cx="74" cy="89" r="1.2"/><circle cx="104" cy="82" r="1.2"/><circle cx="134" cy="72" r="1.2"/><circle cx="164" cy="58" r="1.2"/><circle cx="194" cy="39" r="1.2"/><circle cx="226" cy="18" r="1.2"/></g>
      <polyline fill="none" stroke="#6d8fbf" stroke-width="1" points="44,95 74,93 104,89 134,85 164,80 194,73 226,65"/>
      <g fill="#6d8fbf"><circle cx="44" cy="95" r="1.2"/><circle cx="74" cy="93" r="1.2"/><circle cx="104" cy="89" r="1.2"/><circle cx="134" cy="85" r="1.2"/><circle cx="164" cy="80" r="1.2"/><circle cx="194" cy="73" r="1.2"/><circle cx="226" cy="65" r="1.2"/></g>
      <g font-size="3" fill="#4a5566"><circle cx="92" cy="116" r="1.2" fill="#d98a1a"/><text x="95" y="117">With Outpost Lattice Advisors</text><circle cx="145" cy="116" r="1.2" fill="#6d8fbf"/><text x="148" y="117">Internal hire only</text></g>
      <text x="10" y="132" font-size="2.6" fill="#9aa3b0" font-style="italic">Illustrative model for discussion — not a guarantee of results.</text>
    </svg>
  </div>
  <div class="card" style="left:289px;top:74px;width:150px;height:49px;padding:8px 6px 0 30px"><div class="ico abs" style="left:8px;top:9px;width:15px;height:15px"><svg><use href="#i-bolt"/></svg></div><div class="ct" style="font-size:5px">Productive in weeks</div><div class="cx" style="margin-top:2px">No 12–18 month ramp — the team performs from the start.</div></div>
  <div class="card" style="left:289px;top:130px;width:150px;height:49px;padding:8px 6px 0 30px"><div class="ico abs" style="left:8px;top:9px;width:15px;height:15px"><svg><use href="#i-people"/></svg></div><div class="ct" style="font-size:5px">Network from day one</div><div class="cx" style="margin-top:2px">Immediate access to established broker relationships.</div></div>
  <div class="card" style="left:289px;top:185px;width:150px;height:49px;padding:8px 6px 0 30px"><div class="ico abs" style="left:8px;top:9px;width:15px;height:15px"><svg><use href="#i-shield"/></svg></div><div class="ct" style="font-size:5px">Lower fixed risk</div><div class="cx" style="margin-top:2px">Pay for an outcome-driven team, not a speculative hire.</div></div>
  <div class="foot l">Outpost Lattice Advisors</div><div class="foot r">outpostlatticeadvisors.example &nbsp; <span style="color:var(--orange)">06</span></div>
</section>

<!-- 7 Broker ecosystem -->
<section class="slide dark" style="left:1216px;top:490px">
  <div class="brand">OUTPOST LATTICE ADVISORS</div>
  <div class="eyebrow">Broker Network Access</div>
  <h2 class="title" style="top:32px">Plug into an established franchise broker ecosystem</h2>
  <svg class="abs" style="left:0;top:0" width="461" height="260" viewBox="0 0 461 260">
    <g stroke="#c07a1c" stroke-width=".6" opacity=".8">
      <line x1="230" y1="152" x2="230" y2="98"/><line x1="230" y1="152" x2="120" y2="120"/><line x1="230" y1="152" x2="330" y2="120"/><line x1="230" y1="152" x2="120" y2="186"/><line x1="230" y1="152" x2="330" y2="186"/><line x1="230" y1="152" x2="230" y2="206"/>
    </g>
    <circle cx="230" cy="152" r="24" fill="#1b3660" stroke="#c07a1c" stroke-width=".8" opacity=".6"/>
    <circle cx="230" cy="152" r="18" fill="var(--orange)"/>
    <text x="230" y="153" text-anchor="middle" font-family="Montserrat" font-weight="700" font-size="7" fill="#13294b">OLA</text>
    <text x="230" y="159" text-anchor="middle" font-size="2.6" fill="#13294b">the lattice</text>
  </svg>
  <div class="dcard" style="left:191px;top:70px;width:78px;height:31px;display:flex;align-items:center;padding-left:6px;gap:5px"><div class="ico" style="width:12px;height:12px;flex:none"><svg><use href="#i-share"/></svg></div><div class="ct" style="font-size:3.8px">Referral<br>partners</div></div>
  <div class="dcard" style="left:55px;top:104px;width:72px;height:31px;display:flex;align-items:center;padding-left:6px;gap:5px"><div class="ico" style="width:12px;height:12px;flex:none"><svg><use href="#i-people"/></svg></div><div class="ct" style="font-size:3.8px">Franchise broker networks</div></div>
  <div class="dcard" style="left:328px;top:104px;width:78px;height:31px;display:flex;align-items:center;padding-left:6px;gap:5px"><div class="ico" style="width:12px;height:12px;flex:none"><svg><use href="#i-people"/></svg></div><div class="ct" style="font-size:3.8px">Broker coalitions<br>&amp; events</div></div>
  <div class="abs" style="left:55px;top:171px;width:78px;height:31px;background:var(--orange);border-radius:3px;border:.8px solid #fff3;display:flex;align-items:center;padding-left:6px;gap:5px"><div class="ico" style="width:12px;height:12px;flex:none;background:var(--navy)"><svg><use href="#i-cash"/></svg></div><div class="ct" style="font-size:3.8px;color:var(--navy)">Your franchise<br>brand</div></div>
  <div class="dcard" style="left:328px;top:171px;width:78px;height:31px;display:flex;align-items:center;padding-left:6px;gap:5px"><div class="ico" style="width:12px;height:12px;flex:none"><svg><use href="#i-user"/></svg></div><div class="ct" style="font-size:3.8px">Qualified<br>candidates</div></div>
  <div class="dcard" style="left:191px;top:205px;width:78px;height:31px;display:flex;align-items:center;padding-left:6px;gap:5px"><div class="ico" style="width:12px;height:12px;flex:none"><svg><use href="#i-door"/></svg></div><div class="ct" style="font-size:3.8px">Discovery day<br>pipeline</div></div>
  <div class="brand-foot">OUTPOST LATTICE ADVISORS</div>
  <div class="abs" style="left:131px;bottom:14px;font-size:3.4px;font-style:italic;color:#b9c4d8">Relationships that take years to build — available to your brand from day one.</div>
</section>

<!-- 8 Process -->
<section class="slide" style="left:1749px;top:490px">
  <div class="brand">OUTPOST LATTICE ADVISORS</div>
  <div class="eyebrow">Our Process</div>
  <h2 class="title" style="top:32px">A proven franchise development process</h2>
  <p class="lead" style="left:21px;top:66px;width:400px">A disciplined, repeatable system that turns interest into awarded, conversion-ready franchisees — and keeps your pipeline compounding.</p>
  <svg class="abs" style="left:0;top:0" width="461" height="260"><line x1="59" y1="122" x2="402" y2="122" stroke="#c3c9d2" stroke-width=".6" stroke-dasharray="2 2"/></svg>
  <div class="abs ico" style="left:48px;top:111px;width:22px;height:22px;background:var(--orange);border:2px solid var(--navy);font:700 7px Montserrat;color:var(--navy)">1</div>
  <div class="abs ico" style="left:134px;top:111px;width:22px;height:22px;background:var(--orange);border:2px solid var(--navy);font:700 7px Montserrat;color:var(--navy)">2</div>
  <div class="abs ico" style="left:220px;top:111px;width:22px;height:22px;background:var(--orange);border:2px solid var(--navy);font:700 7px Montserrat;color:var(--navy)">3</div>
  <div class="abs ico" style="left:305px;top:111px;width:22px;height:22px;background:var(--orange);border:2px solid var(--navy);font:700 7px Montserrat;color:var(--navy)">4</div>
  <div class="abs ico" style="left:391px;top:111px;width:22px;height:22px;background:var(--orange);border:2px solid var(--navy);font:700 7px Montserrat;color:var(--navy)">5</div>
  <div class="card center" style="left:21px;top:148px;width:76px;height:77px;padding:8px 4px 0"><div class="ico" style="width:13px;height:13px;margin:0 auto 5px"><svg><use href="#i-search"/></svg></div><div class="ct" style="font-size:4px">Discovery &amp; review</div><div class="cx" style="margin-top:3px;font-size:2.8px">FDD, systems and operations reviewed for scalability.</div></div>
  <div class="card center" style="left:107px;top:148px;width:76px;height:77px;padding:8px 4px 0"><div class="ico" style="width:13px;height:13px;margin:0 auto 5px"><svg><use href="#i-target"/></svg></div><div class="ct" style="font-size:4px">Candidate profiling</div><div class="cx" style="margin-top:3px;font-size:2.8px">Define the ideal franchisee and target market fit.</div></div>
  <div class="card center" style="left:193px;top:148px;width:76px;height:77px;padding:8px 4px 0"><div class="ico" style="width:13px;height:13px;margin:0 auto 5px"><svg><use href="#i-mega"/></svg></div><div class="ct" style="font-size:4px">Generate &amp; activate</div><div class="cx" style="margin-top:3px;font-size:2.8px">Targeted lead generation plus full broker activation.</div></div>
  <div class="card center" style="left:278px;top:148px;width:76px;height:77px;padding:8px 4px 0"><div class="ico" style="width:13px;height:13px;margin:0 auto 5px"><svg><use href="#i-user"/></svg></div><div class="ct" style="font-size:4px">Qualify &amp; discovery day</div><div class="cx" style="margin-top:3px;font-size:2.8px">Vetting, follow-up, and discovery day support.</div></div>
  <div class="card center" style="left:364px;top:148px;width:76px;height:77px;padding:8px 4px 0"><div class="ico" style="width:13px;height:13px;margin:0 auto 5px"><svg><use href="#i-trophy"/></svg></div><div class="ct" style="font-size:4px">Award &amp; scale</div><div class="cx" style="margin-top:3px;font-size:2.8px">Onboard new franchisees and compound the pipeline.</div></div>
  <div class="foot l">Outpost Lattice Advisors</div><div class="foot r">outpostlatticeadvisors.example &nbsp; <span style="color:var(--orange)">08</span></div>
</section>

<!-- 9 Enterprise value -->
<section class="slide" style="left:148px;top:871px">
  <div class="brand">OUTPOST LATTICE ADVISORS</div>
  <div class="eyebrow">Enterprise Value</div>
  <h2 class="title" style="top:32px">How franchise growth compounds into enterprise value</h2>
  <div class="abs" style="right:21px;top:78px;font:600 3.6px Montserrat;color:var(--orange)">Growth compounds +</div>
  <div class="abs center" style="left:21px;top:156px;width:78px;height:76px;background:var(--navy);border-radius:2px;padding:5px 4px 0;color:#fff"><div class="ico" style="width:12px;height:12px;margin:0 auto 4px"><svg><use href="#i-user"/></svg></div><div class="ct" style="font-size:4.2px">Qualified franchisees</div><div class="cx" style="margin-top:8px;font-size:2.8px">A consistent flow of vetted, awarded candidates.</div></div>
  <div class="abs center" style="left:106px;top:139px;width:78px;height:93px;background:var(--blue);border-radius:2px;padding:5px 4px 0;color:#fff"><div class="ico" style="width:12px;height:12px;margin:0 auto 4px"><svg><use href="#i-door"/></svg></div><div class="ct" style="font-size:4.2px;color:#fff">Open units</div><div class="cx" style="margin-top:8px;font-size:2.8px;color:#d0dcef">More territories sold and opened across markets.</div></div>
  <div class="abs center" style="left:191px;top:123px;width:78px;height:109px;background:var(--navy);border-radius:2px;padding:5px 4px 0;color:#fff"><div class="ico" style="width:12px;height:12px;margin:0 auto 4px"><svg><use href="#i-loop"/></svg></div><div class="ct" style="font-size:4.2px;color:#fff">Recurring royalties</div><div class="cx" style="margin-top:8px;font-size:2.8px;color:#aab6cc">Predictable, system-wide royalty revenue.</div></div>
  <div class="abs center" style="left:276px;top:107px;width:78px;height:125px;background:var(--blue);border-radius:2px;padding:5px 4px 0;color:#fff"><div class="ico" style="width:12px;height:12px;margin:0 auto 4px"><svg><use href="#i-chart"/></svg></div><div class="ct" style="font-size:4.2px;color:#fff">Scalable EBITDA</div><div class="cx" style="margin-top:8px;font-size:2.8px;color:#d0dcef">Higher-margin, recurring, defensible earnings.</div></div>
  <div class="abs center" style="left:361px;top:92px;width:78px;height:140px;background:var(--orange);border-radius:2px;padding:5px 4px 0"><div class="ico" style="width:12px;height:12px;margin:0 auto 4px;background:var(--navy)"><svg><use href="#i-gem"/></svg></div><div class="ct" style="font-size:4.2px">Enterprise value</div><div class="cx" style="margin-top:8px;font-size:2.8px;color:var(--navy)">A premium-valued, exit-ready franchise system.</div></div>
  <div class="abs" style="left:0;width:461px;top:240px;text-align:center;font-size:3.4px;font-style:italic;color:var(--muted)">Royalty-based franchise systems earn premium valuations for recurring, scalable, and predictable revenue.</div>
  <div class="foot l">Outpost Lattice Advisors</div><div class="foot r">outpostlatticeadvisors.example &nbsp; <span style="color:var(--orange)">09</span></div>
</section>

<!-- 10 PE & exit -->
<section class="slide dark" style="left:682px;top:871px">
  <div class="eyebrow">Private Equity &amp; Exit</div>
  <h2 class="title" style="top:32px">Building a business that's ready to sell</h2>
  <div class="dcard center" style="left:21px;top:77px;width:67px;height:51px;padding:5px 3px 0"><div class="ico" style="width:12px;height:12px;margin:0 auto 3px"><svg><use href="#i-loop"/></svg></div><div class="ct" style="font-size:4px">Royalty EBITDA</div><div class="cx" style="font-size:2.4px;margin-top:1px">Recurring high-margin earnings</div></div>
  <div class="abs" style="left:93px;top:97px;font:700 8px Montserrat;color:var(--orange)">×</div>
  <div class="dcard center" style="left:106px;top:77px;width:67px;height:51px;padding:5px 3px 0"><div class="ico" style="width:12px;height:12px;margin:0 auto 3px"><svg><use href="#i-chart"/></svg></div><div class="ct" style="font-size:4px">Valuation multiple</div><div class="cx" style="font-size:2.4px;margin-top:1px">Expands as the system scales</div></div>
  <div class="abs" style="left:178px;top:97px;font:700 8px Montserrat;color:var(--orange)">=</div>
  <div class="abs center" style="left:191px;top:77px;width:67px;height:51px;background:var(--orange);border-radius:3px;padding:5px 3px 0"><div class="ico" style="width:12px;height:12px;margin:0 auto 3px;background:var(--navy)"><svg><use href="#i-gem"/></svg></div><div class="ct" style="font-size:4px;color:var(--navy)">Enterprise value</div><div class="cx" style="font-size:2.4px;margin-top:1px;color:var(--navy)">What a buyer will pay</div></div>
  <p class="lead" style="left:21px;top:136px;font-size:3.4px;color:#d3dbe8">Growth lifts both terms at once — driving a multiplicative expansion in enterprise value.</p>
  <div class="abs" style="left:21px;top:163px;font-size:3.3px;line-height:14.5px;color:#d3dbe8">
    <div><span style="display:inline-block;width:4px;height:4px;border-radius:50%;background:var(--orange);vertical-align:middle;margin-right:4px"></span>Unit &amp; system-wide sales growth</div>
    <div><span style="display:inline-block;width:4px;height:4px;border-radius:50%;background:var(--orange);vertical-align:middle;margin-right:4px"></span>Predictable recurring royalties</div>
    <div><span style="display:inline-block;width:4px;height:4px;border-radius:50%;background:var(--orange);vertical-align:middle;margin-right:4px"></span>Strong franchisee validation</div>
    <div><span style="display:inline-block;width:4px;height:4px;border-radius:50%;background:var(--orange);vertical-align:middle;margin-right:4px"></span>Protected market white-space</div>
  </div>
  <div class="dcard" style="left:261px;top:76px;width:178px;height:159px">
    <div class="abs ct" style="left:10px;top:9px;font-size:4px">Illustrative enterprise value as the system scales</div>
    <svg class="abs" style="left:0;top:0" width="178" height="159" viewBox="0 0 178 159">
      <g stroke="#3a5582" stroke-width=".4" stroke-dasharray="1.5 1.5"><line x1="10" y1="46" x2="168" y2="46"/><line x1="10" y1="70" x2="168" y2="70"/><line x1="10" y1="94" x2="168" y2="94"/></g>
      <line x1="10" y1="111" x2="168" y2="111" stroke="#6f80a0" stroke-width=".5"/>
      <rect x="20" y="105" width="10" height="6" fill="var(--orange-soft)"/>
      <rect x="59" y="96" width="10" height="15" fill="var(--orange-soft)"/>
      <rect x="98" y="80" width="10" height="31" fill="var(--orange-soft)"/>
      <rect x="137" y="47" width="10" height="64" fill="var(--orange-soft)"/>
      <g font-size="3" fill="#fff" text-anchor="middle" font-weight="700"><text x="25" y="103">12</text><text x="64" y="94">38</text><text x="103" y="78">84</text><text x="142" y="45">175</text></g>
      <g font-size="3" fill="#aab6cc" text-anchor="middle"><text x="25" y="120">1</text><text x="64" y="120">2</text><text x="103" y="120">3</text><text x="142" y="120">4</text></g>
      <text x="10" y="152" font-size="2.4" fill="#6f80a0" font-style="italic">Relative enterprise value ($M, illustrative). For discussion only.</text>
    </svg>
  </div>
  <div class="brand-foot">OUTPOST LATTICE ADVISORS</div>
</section>

<!-- 11 Engagement -->
<section class="slide" style="left:1216px;top:871px">
  <div class="brand">OUTPOST LATTICE ADVISORS</div>
  <div class="eyebrow">How We Partner</div>
  <h2 class="title" style="top:32px">A flexible engagement built around your growth goals</h2>
  <div class="card" style="left:21px;top:90px;width:131px;height:62px;padding:8px 7px 0"><div class="ico abs" style="left:8px;top:8px;width:14px;height:14px"><svg><use href="#i-people"/></svg></div><div class="ct" style="font-size:4.4px;margin-left:21px">Dedicated sales team</div><div class="cx" style="margin-top:15px;font-size:2.8px">A fractional franchise development team acting as an extension of your brand.</div></div>
  <div class="card" style="left:164px;top:90px;width:131px;height:62px;padding:8px 7px 0"><div class="ico abs" style="left:8px;top:8px;width:14px;height:14px"><svg><use href="#i-net"/></svg></div><div class="ct" style="font-size:4.4px;margin-left:21px">Broker activation</div><div class="cx" style="margin-top:15px;font-size:2.8px">Immediate engagement of established broker and referral networks.</div></div>
  <div class="card" style="left:306px;top:90px;width:132px;height:62px;padding:8px 7px 0"><div class="ico abs" style="left:8px;top:8px;width:14px;height:14px"><svg><use href="#i-search"/></svg></div><div class="ct" style="font-size:4.4px;margin-left:21px">Full-funnel management</div><div class="cx" style="margin-top:15px;font-size:2.8px">Lead generation through qualification, discovery day, and award.</div></div>
  <div class="card" style="left:21px;top:163px;width:131px;height:63px;padding:8px 7px 0"><div class="ico abs" style="left:8px;top:8px;width:14px;height:14px"><svg><use href="#i-doc"/></svg></div><div class="ct" style="font-size:4.4px;margin-left:21px">Reporting &amp;<br>accountability</div><div class="cx" style="margin-top:10px;font-size:2.8px">Transparent pipeline reporting tied directly to results.</div></div>
  <div class="card" style="left:164px;top:163px;width:131px;height:63px;padding:8px 7px 0"><div class="ico abs" style="left:8px;top:8px;width:14px;height:14px"><svg><use href="#i-pin"/></svg></div><div class="ct" style="font-size:4.4px;margin-left:21px">Multi-market expansion</div><div class="cx" style="margin-top:15px;font-size:2.8px">Strategy and execution for scaling across new territories.</div></div>
  <div class="card" style="left:306px;top:163px;width:132px;height:63px;padding:8px 7px 0"><div class="ico abs" style="left:8px;top:8px;width:14px;height:14px"><svg><use href="#i-rocket"/></svg></div><div class="ct" style="font-size:4.4px;margin-left:21px">Growth strategy</div><div class="cx" style="margin-top:15px;font-size:2.8px">Long-term development planning that builds enterprise value.</div></div>
  <div class="foot l">Outpost Lattice Advisors</div><div class="foot r">outpostlatticeadvisors.example &nbsp; <span style="color:var(--orange)">11</span></div>
</section>

<!-- 12 Why us -->
<section class="slide dark" style="left:1749px;top:871px">
  <div class="eyebrow" style="top:23px">Why Outpost Lattice Advisors</div>
  <h2 class="title" style="top:32px">The partner built to scale your franchise</h2>
  <div class="dcard center" style="left:21px;top:95px;width:97px;height:110px;padding:14px 6px 0"><div class="ico" style="width:22px;height:22px;margin:0 auto 8px"><svg><use href="#i-medal"/></svg></div><div class="ct" style="color:var(--orange);font-size:5.6px">Experience</div><div class="cx" style="margin-top:4px">30+ years and 550+ franchise sales behind every engagement.</div></div>
  <div class="dcard center" style="left:128px;top:95px;width:97px;height:110px;padding:14px 6px 0"><div class="ico" style="width:22px;height:22px;margin:0 auto 8px"><svg><use href="#i-net"/></svg></div><div class="ct" style="color:var(--orange);font-size:5.6px">Network</div><div class="cx" style="margin-top:4px">An established broker ecosystem, available from day one.</div></div>
  <div class="dcard center" style="left:235px;top:95px;width:97px;height:110px;padding:14px 6px 0"><div class="ico" style="width:22px;height:22px;margin:0 auto 8px"><svg><use href="#i-gear"/></svg></div><div class="ct" style="color:var(--orange);font-size:5.6px">Process</div><div class="cx" style="margin-top:4px">A proven, repeatable development system — not ad-hoc selling.</div></div>
  <div class="dcard center" style="left:342px;top:95px;width:97px;height:110px;padding:14px 6px 0"><div class="ico" style="width:22px;height:22px;margin:0 auto 8px"><svg><use href="#i-gem"/></svg></div><div class="ct" style="color:var(--orange);font-size:5.6px">Outcome</div><div class="cx" style="margin-top:4px">Enterprise value creation and an exit-ready franchise system.</div></div>
  <div class="brand-foot">OUTPOST LATTICE ADVISORS</div>
  <div class="foot r">outpostlatticeadvisors.example &nbsp; <span style="color:var(--orange)">12</span></div>
</section>

<!-- 13 CTA -->
<section class="slide dark" style="left:148px;top:1252px">
  <div class="eyebrow" style="top:54px">Let's Build Your Growth Engine</div>
  <h2 class="abs" style="left:21px;top:68px;font:700 22px 'Montserrat',sans-serif;color:#fff">Book a strategy call</h2>
  <p class="lead" style="left:21px;top:108px;width:270px;color:#d3dbe8">Let's map your franchise growth plan — qualified candidates, broker access, and a development engine built to scale and create enterprise value.</p>
  <div class="abs" style="left:21px;top:160px;font-size:4px;line-height:23px;color:#fff">
    <div style="display:flex;align-items:center;gap:8px"><span class="ico" style="width:12px;height:12px"><svg><use href="#i-globe"/></svg></span>www.outpostlatticeadvisors.example</div>
    <div style="display:flex;align-items:center;gap:8px"><span class="ico" style="width:12px;height:12px"><svg><use href="#i-mail"/></svg></span>info@outpostlatticeadvisors.example</div>
    <div style="display:flex;align-items:center;gap:8px"><span class="ico" style="width:12px;height:12px"><svg><use href="#i-pin"/></svg></span>418 Harbor Line Ave., Ste 3, Fairview, ST 00000</div>
  </div>
  <div class="abs" style="left:21px;top:232px;width:104px;height:22px;border-radius:11px;background:var(--orange);font:700 4.6px/22px 'Montserrat',sans-serif;color:var(--navy);text-align:center">Schedule a Free Call</div>
  <div class="abs" style="left:135px;top:240px;font:700 5.5px 'Montserrat',sans-serif;color:#fff;letter-spacing:.3px">OUTPOST LATTICE ADVISORS</div>
</section>

</main>
</body>
</html>
```